Granite Surface Works, Inc. Business Card

New business, we do epoxy, polishing concrete, underlayment, fluid applied flooring, sound proofing, double sided, will need 3 sets of cards with 3 different names and phone numbers.
Company: Granite Surface Works, Inc.
Address and Phone: 6339 Charlotte Pike PMB 2183Nashville, TN 37209
(615) 384-7190
www.granitesurfaceworks.example

Target Market(s)

General Contractors, Contractors, Architects

Contact Information for Business Card

1st Card: Derek Halvorsen C. 708.214.8573 e. derek@granitesurfaceworks.example
Vice President
2nd Card: Morgan Brasfield C. 708.361.5847 e. morgan@granitesurfaceworks.example
President
3rd Card: Raj Oti C. 405.617.3328 e. raj@granitesurfaceworks.example
Managing Partner

Font styles to use
Serif
Sans Serif

Requirements
Must have
• Professional Clean Design, Implement colors from Logo or nicely contrasting
Nice to have
• N/A

```html
<!DOCTYPE html>
<html lang="en">
<head>
<meta charset="utf-8">
<title>Granite Surface Works, Inc. Business Card</title>
<link rel="stylesheet" href="https://fonts.googleapis.com/css2?family=Poppins:wght@400;500;600;700&display=swap">
<style>
  :root {
    --stage: #2b2b2d;
    --brand-blue: #0c63b8;
    --brand-teal: #2f8a95;
    --brand-green: #6aae4f;
    --accent-green: #5aab3c;
    --floor-purple: #6b5478;
    --floor-purple-light: #83709a;
    --ink: #1d1d1f;
    --paper: #ffffff;
    --rule: #2a2a2a;
  }
  * { box-sizing: border-box; margin: 0; padding: 0; }
  html, body { width: 1200px; height: 900px; overflow: hidden; }
  body {
    background: var(--stage);
    font-family: "Poppins", sans-serif;
    position: relative;
  }
  .card {
    position: absolute;
    left: 250px;
    width: 700px;
    height: 400px;
    border-radius: 22px;
    overflow: hidden;
  }
  /* Front side */
  .card--front { top: 35px; }
  .front-backdrop {
    position: absolute; inset: 0;
    background: linear-gradient(30deg, var(--brand-blue) 0%, var(--brand-teal) 55%, var(--brand-green) 100%);
  }
  .front-brand {
    position: absolute;
    left: 0; right: 0; top: 125px;
    display: flex; flex-direction: column; align-items: center; gap: 16px;
  }
  .brand-square {
    width: 70px; height: 70px;
    border: 8px solid var(--paper);
  }
  .front-brand .brand-name {
    color: var(--paper);
    font-size: 30px; font-weight: 500;
    letter-spacing: 3px;
    text-transform: uppercase;
  }
  .service-list {
    position: absolute;
    left: 0; right: 0; bottom: 40px;
    text-align: center;
    color: var(--paper);
    font-size: 14px; font-weight: 600;
    letter-spacing: 0.8px;
    text-transform: uppercase;
  }
  /* Back side */
  .card--back { top: 465px; background: var(--paper); }
  .floor-photo {
    position: absolute; left: 0; top: 0;
    width: 100%; height: 170px;
    background: linear-gradient(180deg, var(--floor-purple-light) 0%, var(--floor-purple) 100%);
  }
  .logo-panel {
    position: absolute;
    left: 40px; top: 50px;
    width: 210px; height: 190px;
    background: var(--paper);
    display: flex; flex-direction: column; align-items: center; justify-content: center; gap: 14px;
    padding: 0 14px;
  }
  .logo-panel .brand-square { border-color: var(--brand-blue); width: 56px; height: 56px; border-width: 7px; }
  .logo-panel .brand-name {
    color: var(--ink);
    font-size: 17px; font-weight: 600;
    letter-spacing: 1px;
    text-transform: uppercase;
    text-align: center;
    line-height: 1.3;
  }
  .person {
    position: absolute; right: 48px; top: 44px;
    text-align: right;
  }
  .person-name {
    color: var(--paper);
    font-size: 22px; font-weight: 600;
    letter-spacing: 1px; text-transform: uppercase;
  }
  .person-title {
    color: var(--accent-green);
    font-size: 15px; font-weight: 500;
    letter-spacing: 1px; text-transform: uppercase;
    padding-bottom: 6px;
    border-bottom: 3px solid var(--accent-green);
    display: inline-block;
  }
  .contact-line {
    display: flex; align-items: center; gap: 10px;
    font-size: 16px; color: var(--ink);
    line-height: 1.6;
  }
  .contact-line svg { width: 18px; height: 18px; flex: none; }
  .personal-contacts {
    position: absolute; right: 40px; top: 182px;
    display: flex; flex-direction: column; align-items: flex-end;
  }
  .rule-right {
    position: absolute; left: 300px; right: 30px; top: 248px;
    border-top: 1.5px solid var(--rule);
  }
  .office-address {
    position: absolute; right: 40px; top: 258px;
    text-align: right; font-size: 16px; color: var(--ink); line-height: 1.5;
    display: flex; gap: 10px; align-items: flex-start;
  }
  .office-address svg { width: 18px; height: 22px; margin-top: 3px; }
  .rule-left {
    position: absolute; left: 0; width: 330px; top: 300px;
    border-top: 1.5px solid var(--rule);
  }
  .company-contacts {
    position: absolute; left: 40px; top: 310px;
  }
  .brand-band {
    position: absolute; left: 0; right: 0; bottom: 0; height: 14px;
    background: linear-gradient(90deg, var(--accent-green) 0%, var(--accent-green) 45%, var(--brand-teal) 65%, var(--brand-blue) 100%);
  }
</style>
</head>
<body>

<section class="card card--front" aria-label="Card front">
  <div class="front-backdrop" role="img" aria-label="Blue to green gradient with soft reflections of window light on a polished floor"></div>
  <div class="front-brand">
    <span class="brand-square"></span>
    <span class="brand-name">Granite Surface Works</span>
  </div>
  <p class="service-list">Epoxy • Polishing Concrete • Underlayment • Fluid Applied Flooring • Sound Proofing</p>
</section>

<section class="card card--back" aria-label="Card back">
  <div class="floor-photo" role="img" aria-label="Photo of a polished purple-toned concrete floor in a large hall"></div>

  <div class="logo-panel">
    <span class="brand-square"></span>
    <span class="brand-name">Granite Surface Works</span>
  </div>

  <div class="person">
    <p class="person-name">Derek Halvorsen</p>
    <p class="person-title">Vice President</p>
  </div>

  <div class="personal-contacts">
    <p class="contact-line">708.214.8573
      <svg viewBox="0 0 18 18" aria-hidden="true"><rect x="4" y="1" width="10" height="16" rx="2" fill="none" stroke="var(--accent-green)" stroke-width="2"/><circle cx="9" cy="14" r="1" fill="var(--accent-green)"/></svg>
    </p>
    <p class="contact-line">derek@granitesurfaceworks.example
      <svg viewBox="0 0 18 18" aria-hidden="true"><rect x="1" y="4" width="16" height="11" fill="var(--accent-green)"/><path d="M1 4 L9 10 L17 4" fill="none" stroke="var(--paper)" stroke-width="1.5"/></svg>
    </p>
  </div>

  <div class="rule-right"></div>

  <div class="office-address">
    <p>4817 Willowmere Road PMB 5046<br>Nashville, TN 37209</p>
    <svg viewBox="0 0 18 22" aria-hidden="true"><path d="M9 1 C4.5 1 1.5 4.3 1.5 8.3 C1.5 13.5 9 21 9 21 C9 21 16.5 13.5 16.5 8.3 C16.5 4.3 13.5 1 9 1 Z" fill="var(--accent-green)"/><circle cx="9" cy="8.3" r="2.8" fill="var(--paper)"/></svg>
  </div>

  <div class="rule-left"></div>

  <div class="company-contacts">
    <p class="contact-line">
      <svg viewBox="0 0 18 18" aria-hidden="true"><path d="M4 1.5 L7 4.5 L5.3 6.5 C6.3 8.8 8.5 11 11 12.5 L13 10.8 L16.3 13.8 L14 16.5 C8 16 2 10 1.5 4 Z" fill="var(--accent-green)"/></svg>
      (615) 384-7190
    </p>
    <p class="contact-line">
      <svg viewBox="0 0 18 18" aria-hidden="true"><g fill="none" stroke="var(--accent-green)" stroke-width="1.5"><circle cx="9" cy="9" r="7.5"/><ellipse cx="9" cy="9" rx="3.2" ry="7.5"/><path d="M1.5 9 H16.5 M3 5 H15 M3 13 H15"/></g></svg>
      www.granitesurfaceworks.example
    </p>
  </div>

  <div class="brand-band"></div>
</section>

</body>
</html>
```